Strand Wire Outlet line card

This will be a pretty simple one to design. We are an online company that sells fiber optic and copper cables and we would like a line card designed for us. I've included all the information to go on the line card as well as the (2) images that should be included. I've put all the information on a Word doc (linecard.doc) but it doesn't have to have this exact layout. Feel free to add image(s) if you think its appropriate. I would like the line card to be easy to read yet creative. We will be emailing this to thousands of customers. Phone number should be prominent.

I've added a few more images for you to work with. I realized that there was too much text and not enough images. Again, feel free to use your own as well and you don't have to use them all. Good luck!

Target Market(s)

Small to medium sized businesses. Government, Military and Educational institutions.

Industry/Entity Type

It Company

Colors

Designer to choose colors to be used in the design.

Requirements
Must have
• One page design. Clear and easy to read

```html
<!DOCTYPE html>
<html lang="en">
<head>
<meta charset="utf-8">
<title>Strand Wire Outlet — Line Card</title>
<link href="https://fonts.googleapis.com/css2?family=Roboto+Condensed:wght@400;700&family=Arimo:wght@400;700&display=swap" rel="stylesheet">
<style>
  :root{
    --blue:#1b82d4;
    --blue-dark:#1463a8;
    --red:#d2232a;
    --page:#efefef;
    --panel:#ffffff;
    --band:#e6e6e6;
    --ink:#262626;
    --muted:#6b6b6b;
    --panel-line:#b9d4ea;
  }
  html,body{margin:0;padding:0;overflow:hidden;}
  body{width:928px;height:1200px;background:var(--page);font-family:"Roboto Condensed",Arial Narrow,sans-serif;color:var(--ink);}
  .card{position:relative;width:928px;height:1200px;overflow:hidden;background:var(--page);}

  .brand{position:absolute;left:70px;top:22px;display:flex;align-items:center;gap:16px;}
  .brand-dot{width:40px;height:40px;border-radius:50%;background:var(--blue);flex:none;}
  .brand-name{font-family:"Roboto Condensed",sans-serif;font-weight:700;color:var(--red);font-size:56px;line-height:54px;letter-spacing:-1px;}

  .title-block{position:absolute;left:497px;top:0;width:431px;height:176px;background:var(--blue);display:flex;align-items:center;justify-content:center;}
  .title-block h1{margin:0;font-family:"Arimo",Arial,sans-serif;font-weight:400;color:#fff;font-size:66px;letter-spacing:1px;}

  .panel{position:absolute;background:var(--panel);border:1px solid var(--panel-line);box-shadow:0 10px 14px -8px rgba(0,0,0,.25);}
  .panel h2{margin:0;font-weight:400;font-size:25px;letter-spacing:.3px;}
  .panel ul{list-style:none;margin:0;padding:0;}
  .panel li{font-size:17px;height:24.7px;line-height:24.7px;padding-left:8px;}
  .panel li:nth-child(odd){background:var(--band);}
  .panel li.sub{padding-left:48px;position:relative;}
  .panel li.sub::before{content:"";position:absolute;left:31px;top:10px;width:6px;height:6px;border-radius:50%;background:var(--ink);}

  .fiber{left:41px;top:211px;width:860px;height:390px;}
  .fiber h2{position:absolute;left:24px;top:14px;color:var(--blue);}
  .fiber .col-left{position:absolute;left:26px;top:53px;width:438px;}
  .fiber .col-right{position:absolute;left:483px;top:53px;width:354px;}

  .copper{left:41px;top:636px;width:423px;height:344px;}
  .copper h2{position:absolute;left:19px;top:18px;color:var(--blue);}
  .copper ul{position:absolute;left:16px;top:56px;width:373px;}

  .connector-photo{position:absolute;left:470px;top:585px;width:458px;height:250px;
    background:linear-gradient(120deg,#ffffff 0%,#cfe3f2 25%,#3b78c4 45%,#2f9a4c 62%,#d8362f 80%,#f3c23a 100%);opacity:.9;}

  .capabilities{left:496px;top:780px;width:405px;height:198px;border-color:#e8b3b5;}
  .capabilities h2{position:absolute;left:20px;top:18px;color:var(--red);}
  .capabilities ul{position:absolute;left:16px;top:59px;width:373px;}

  .stock-badge{position:absolute;left:365px;top:568px;width:174px;height:174px;border-radius:50%;background:var(--red);border:4px solid #fff;box-sizing:border-box;color:#fff;text-align:center;z-index:5;box-shadow:0 4px 10px rgba(0,0,0,.2);}
  .stock-badge .over{display:block;margin-top:16px;font-size:18px;font-weight:700;line-height:18px;}
  .stock-badge .count{display:block;font-size:44px;font-weight:700;line-height:42px;letter-spacing:-1px;}
  .stock-badge .unit{display:block;font-size:18px;font-weight:700;line-height:20px;}
  .stock-badge .ship{display:block;font-size:15.5px;line-height:18px;margin-top:6px;}

  .origin-seal{position:absolute;left:20px;top:998px;width:88px;height:88px;border-radius:50%;background:radial-gradient(circle at 40% 35%,#e0575c,#b3161c);}
  .pricing{position:absolute;right:470px;top:1018px;text-align:right;color:var(--muted);font-size:20px;line-height:29px;letter-spacing:.3px;text-transform:uppercase;margin:0;}

  .contract{position:absolute;left:0;top:1096px;width:452px;height:87px;background:#fff;}
  .contract-mark{position:absolute;left:58px;top:14px;width:40px;height:40px;background:var(--blue-dark);}
  .contract-label{position:absolute;left:106px;top:20px;font-family:"Arimo",Arial,sans-serif;font-size:20px;color:#333;}
  .contract-note{position:absolute;left:58px;top:62px;font-size:13.5px;color:var(--blue-dark);letter-spacing:.2px;text-transform:uppercase;}

  .contact{position:absolute;left:497px;top:1015px;width:431px;height:185px;background:var(--blue);color:#fff;font-family:"Roboto Condensed",Arial Narrow,sans-serif;font-weight:700;font-size:21px;line-height:26px;letter-spacing:.4px;}
  .contact p{margin:0;}
  .contact .lines{position:absolute;left:31px;top:24px;}
  .contact .address{position:absolute;left:31px;top:108px;}
</style>
</head>
<body>
<main class="card">

  <header class="brand">
    <span class="brand-dot"></span>
    <span class="brand-name">Strand Wire<br>Outlet</span>
  </header>

  <div class="title-block"><h1>LINE CARD</h1></div>

  <section class="panel fiber">
    <h2>FIBER PRODUCTS</h2>
    <ul class="col-left">
      <li>Fiber Jumpers (LC, SC, ST, FC, MTRJ)</li>
      <li class="sub">Singlemode</li>
      <li class="sub">Multimode (62.5/125 &amp; 50/125)</li>
      <li class="sub">OM3 &amp; OM4 10Gb Aqua cables</li>
      <li>Multifiber Assemblies (2, 4, 6, 8, 12, 24, 48, 96, 144 fiber)</li>
      <li class="sub">Indoor/Outdoor</li>
      <li class="sub">Direct Burial</li>
      <li class="sub">Tactical</li>
      <li class="sub">Armored</li>
      <li class="sub">Aerial</li>
      <li>MXP/MPO Trunks</li>
      <li>Angle Polish (APC) Cables (LC, SC, ST)</li>
      <li>Attenuators (LC, SC, ST)</li>
    </ul>
    <ul class="col-right">
      <li>Fiber Pigtails</li>
      <li>Mode Conditioning Cables (LC, SC, ST)</li>
      <li>LC Uniboot Cables</li>
      <li>Launch Boxes</li>
      <li>Colored Fiber Cables</li>
      <li>Fiber Couplers (SC, ST, LC)</li>
      <li>Fiber Adapters (SC, ST, LC)</li>
      <li>SMA 905/906</li>
      <li>FDDI, Escara, Biconic, D4 connectors</li>
      <li>Lumijack, Lumiplug Connectors</li>
      <li>Fiber Adapter Panels</li>
      <li>Fiber Breakout Modules</li>
      <li>Enclosures, Panels &amp; Wall Mount Boxes</li>
    </ul>
  </section>

  <div class="connector-photo" role="img" aria-label="Close-up of colourful fiber optic connectors in blue, green, red and yellow"></div>

  <div class="stock-badge">
    <span class="over">OVER</span>
    <span class="count">100,000</span>
    <span class="unit">CABLES IN STOCK</span>
    <span class="ship">Same day shipping<br>available</span>
  </div>

  <section class="panel copper">
    <h2>COPPER PRODUCTS</h2>
    <ul>
      <li>Cat5e, Cat6 and Cat6A patch cables</li>
      <li>Cat5e, Cat6 and Cat6A bulk cable</li>
      <li>Power Cables</li>
      <li>DS3, DS4, E3 and T3 cables</li>
      <li>Hydra assemblies</li>
      <li>Telco assemblies</li>
      <li>Twinax assemblies</li>
      <li>HDMI cables</li>
      <li>Audio/Video cables</li>
      <li>Netvale cables</li>
      <li>Modular adapters</li>
    </ul>
  </section>

  <section class="panel capabilities">
    <h2>CAPABILITIES</h2>
    <ul>
      <li>Fiber Testing</li>
      <li>Serialized Labeling</li>
      <li>Custom Packaging</li>
      <li>Pulling eyes, breakout kits</li>
      <li>Made in the U.S.A custom cables</li>
    </ul>
  </section>

  <div class="origin-seal" role="img" aria-label="Made in USA seal"></div>
  <p class="pricing">Government, Education &amp; Reseller<br>Preferred Pricing Available</p>

  <div class="contract">
    <span class="contract-mark"></span>
    <span class="contract-label">Contract Holder</span>
    <span class="contract-note">A woman-owned, minority-owned small business</span>
  </div>

  <footer class="contact">
    <div class="lines">
      <p>PHONE: (866) 555-0142</p>
      <p>FAX (949) 555-0187</p>
    </div>
    <div class="address">
      <p>214 MERIDIAN WAY, LAKEPORT, NV 89502</p>
      <p>SALES@STRANDWIREOUTLET.COM</p>
    </div>
  </footer>

</main>
</body>
</html>
```